Geschäftspapiere für Coaching und Talent Management
Professionell und freundlich
Zielgruppe
Zielgruppe: Führungskräfte
Tätigkeit: Führungskräfte Coaching und Talent Management
Aufgabenstellung
- Der Briefbogen soll klar und smart/elegant wirken
- Das Logo wurde gerade neu erstellt und füge ich bei
- Die weiteren Daten lade ich hoch sobald der Gewinner gewählt ist. Bitte beim Design beachten, dass folg Informationen zusätzlich zum Logo auf das Briefpapier sollen:
Postleitzahl und Stadt
Strasse und Hausnummer
Website und Email Kontakt
Umsatz St.Nr

```html
<!DOCTYPE html>
<html lang="de">
<head>
<meta charset="utf-8">
<title>Briefbogen – Marlene Roth</title>
<link rel="stylesheet" href="https://fonts.googleapis.com/css2?family=Source+Sans+3:wght@400;600&family=EB+Garamond&display=swap">
<style>
  :root {
    --bg: #e4e4e4;
    --paper: #ffffff;
    --accent-red: #c9432b;
    --accent-teal: #0f4650;
    --ink: #2a2a2a;
    --muted: #8a8a8a;
    --signature-ink: #2b2a72;
  }
  html, body {
    margin: 0;
    width: 1200px;
    height: 1105px;
    overflow: hidden;
    background: var(--bg);
    font-family: "Source Sans 3", sans-serif;
  }
  .letterhead {
    position: absolute;
    left: 232px;
    top: 32px;
    width: 736px;
    height: 1040px;
    background: var(--paper);
    box-shadow: 0 2px 10px rgba(0,0,0,0.12);
    color: var(--ink);
  }
  .edge-stripe { position: absolute; top: 0; bottom: 0; width: 6px; }
  .edge-stripe--red { left: 10px; background: var(--accent-red); }
  .edge-stripe--teal { left: 22px; background: var(--accent-teal); }
  .fold-mark {
    position: absolute; left: 34px; width: 0; height: 0;
    border-top: 3px solid transparent; border-bottom: 3px solid transparent;
    border-left: 5px solid var(--accent-red);
  }
  .brand {
    position: absolute; top: 78px; left: 300px;
    display: flex; align-items: center; gap: 10px;
  }
  .brand-dot { width: 22px; height: 22px; border-radius: 50%; background: var(--accent-teal); }
  .brand-rule { width: 1px; height: 34px; background: var(--accent-teal); }
  .brand-name {
    font-size: 21px; font-weight: 400; letter-spacing: 2px;
    color: var(--accent-red); line-height: 1;
  }
  .brand-tagline {
    font-size: 9px; letter-spacing: 5.6px; color: var(--accent-teal);
    margin-top: 2px;
  }
  .contact-line {
    position: absolute; top: 128px; left: 200px; right: 40px;
    font-size: 8px; color: var(--muted); display: flex; gap: 18px;
  }
  .contact-line b { color: #555; font-weight: 600; }
  .address-window { position: absolute; left: 80px; top: 160px; width: 320px; height: 150px; }
  .address-window svg { position: absolute; inset: 0; }
  .sender-line {
    position: absolute; left: 90px; top: 26px; width: 200px;
    font-size: 7.5px; color: var(--muted);
    border-bottom: 1px solid #999; padding-bottom: 3px;
  }
  .recipient {
    position: absolute; left: 20px; top: 48px;
    font-size: 10px; line-height: 1.2; font-weight: 600;
  }
  .letter-body {
    position: absolute; left: 80px; right: 56px; top: 372px;
    font-size: 14.5px; line-height: 1.22;
  }
  .letter-body p { margin: 0 0 16px; text-align: justify; hyphens: auto; }
  .letter-body .salutation { margin-bottom: 12px; text-align: left; }
  .signature-block { position: absolute; left: 420px; top: 880px; width: 240px; }
  .signature-mark {
    width: 200px; height: 40px; border-radius: 20px;
    background: linear-gradient(90deg, rgba(43,42,114,0.12), rgba(43,42,114,0.04));
  }
  .signer-name {
    font-family: "EB Garamond", serif; font-size: 13px; letter-spacing: 0.5px;
    margin: 2px 0 0 40px; color: #444;
  }
  .signer-role { font-family: "EB Garamond", serif; font-size: 13px; margin-left: 40px; color: #444; }
  .footer {
    position: absolute; left: 220px; right: 40px; bottom: 36px;
    font-size: 8px; color: var(--muted); line-height: 1.6;
  }
  .footer b { color: #555; font-weight: 600; }
</style>
</head>
<body>
<main class="letterhead">
  <div class="edge-stripe edge-stripe--red"></div>
  <div class="edge-stripe edge-stripe--teal"></div>
  <span class="fold-mark" style="top:340px"></span>
  <span class="fold-mark" style="top:700px"></span>

  <header class="brand">
    <span class="brand-dot"></span>
    <span class="brand-rule"></span>
    <div>
      <div class="brand-name">MARLENE ROTH</div>
      <div class="brand-tagline">THE LEADERSHIP COACH</div>
    </div>
  </header>

  <div class="contact-line">
    <span>Am Lindenhof 7 - 61000 Talbach</span>
    <span><b>Telefon:</b> +49 0000 41270 - 0 - <b>E-Mail:</b> info@roth-coaching.de</span>
  </div>

  <section class="address-window">
    <svg width="320" height="150" viewBox="0 0 320 150" fill="none" stroke="#555" stroke-width="1">
      <path d="M0 22 Q0 4 18 4 L24 4"/>
      <path d="M296 4 L302 4 Q320 4 320 22"/>
      <path d="M0 128 Q0 146 18 146 L24 146"/>
      <path d="M296 146 L302 146 Q320 146 320 128"/>
    </svg>
    <div class="sender-line">Am Lindenhof 7 - 61000 Talbach</div>
    <div class="recipient">Herr.:<br>Jonas Weller<br>Web Master<br>City</div>
  </section>

  <article class="letter-body">
    <p class="salutation">Lorem ipsum dolor sit amet,</p>
    <p>Lorem ipsum dolor sit amet, consectetur adipiscing elit. Donec orci purus, luctus vitae dignissim eu, iaculis sed purus. Vivamus faucibus, ipsum nec aliquet viverra, leo mauris condimentum ligula, sit amet sagittis enim ligula quis arcu. Nam egestas tortor id nisi porttitor mattis. In tortor ante, ultricies in suscipit a, tempus non massa. Vivamus et auctor mi. Fusce vel massa nulla. Phasellus nec eros mauris, et scelerisque orci. Donec malesuada orci vitae nulla accumsan porta a id massa. Quisque accumsan iaculis magna sit amet fringilla. Maecenas consequat, magna eget tincidunt semper, odio nibh rutrum mi, id feugiat ante nisi eu risus. Vestibulum nunc orci, rhoncus a placerat in, ultricies in mi. Cras mattis varius eros, vel fringilla nisi suscipit eget.</p>
    <p>Quisque scelerisque sagittis nulla at porttitor. Mauris a justo et tellus interdum tristique. Sed id augue vitae urna euismod commodo aliquet a quam. Pellentesque arcu velit, cursus et malesuada ut, consequat et diam. Nullam erat sem, rhoncus id ullamcorper vitae, rhoncus et arcu. In ultricies ultricies nulla, ut rutrum nisi iaculis at. Donec eu magna a metus ornare faucibus. Fusce aliquet faucibus ultricies. Morbi semper, est id tincidunt gravida, sem arcu adipiscing lacus, ac bibendum nulla leo eu purus. Quisque nec diam sed risus consectetur accumsan quis quis nibh. Vestibulum id purus lorem.</p>
    <p>Vivamus vehicula accumsan lacinia. Aliquam erat volutpat. Pellentesque consequat venenatis velit non gravida. Etiam et sem et nulla congue aliquam sed eget augue. Nulla facilisi. Pellentesque habitant morbi tristique senectus et netus et malesuada fames ac turpis egestas. Nulla a elit at sem iaculis congue. Nullam mollis tristique lobortis.</p>
  </article>

  <div class="signature-block">
    <div class="signature-mark" role="img" aria-label="Handschriftliche Unterschrift"></div>
    <div class="signer-name">CLARA MENZ</div>
    <div class="signer-role">Manager</div>
  </div>

  <footer class="footer">
    <div><b>Bankverbindung:</b> Talbank eG - IBAN: DE20 0000 0240 0507 0012 88 - BIC: TALBDE51XXX</div>
    <div><b>Handelsregister:</b> Amtsgericht Talbach - HRA 00000 - USt-IdNr: DE41 0000 000</div>
  </footer>
</main>
</body>
</html>
```